Commercial brochure presenting independent commercial activity

I would like to create a commercial brochure for my new professional activity.

This is a personal and not business oriented brochure because I will become an independent project assistant to assist engineering offices with one-off missions.

I want a 4 page A4 brochure

• Page 1: Logo, personal photo
• Page 2 and 3: Personal presentation and presentation of my activities
• Page4: contact information

My target audience: engineering offices and design offices

The objective of the brochure: it is to make my profile interesting so that design offices will want to use my services when there is demand

Sector of activity: food, chemical, pharmaceutical industry
The text of the brochure must remain in French and contain what is in the attached file

On page 1, you must keep a space for a photo of my profile which I will insert later because I do not have it yet and insert my monogram (it can be reworked to be inserted in the brochure)
The image with the logo (R/M) is the color range I want

Target Market(s)

engineering offices and design offices

Industry/Entity Type

industrie alimentaire, chimique, pharmaceutique

Font styles to use
Sans Serif

Colors
0094D4
00A9DD
6FCCEA
C7EBF8
E9F6FB

Requirements
Must have
• The plate must comply with current codes. Each reader must think that I am dynamic and that my services are of quality and equivalent to the presentation

```html
<!DOCTYPE html>
<html lang="fr">
<head>
<meta charset="utf-8">
<title>Lucien Maréchal-Dorval – Assistant de projet indépendant</title>
<link rel="stylesheet" href="https://fonts.googleapis.com/css2?family=Ubuntu:ital,wght@0,300;0,400;0,500;0,700;1,400&display=swap">
<style>
  :root{
    --brand-blue:#0094d4;
    --brand-cyan:#00a9dd;
    --brand-sky:#6fccea;
    --brand-ice:#c7ebf8;
    --brand-mist:#e9f6fb;
    --ink-navy:#1c4e86;
    --ink-body:#5a5f66;
    --deep-blue:#1d5d92;
    --sheet:#ffffff;
    --stage:#5b5b5b;
    --wave-grey:#b9bcc0;
  }
  *{box-sizing:border-box;margin:0;padding:0}
  html,body{width:1156px;height:1200px;overflow:hidden;background:var(--stage)}
  body{font-family:"Ubuntu",sans-serif;color:var(--ink-body)}
  .spread{
    display:grid;grid-template-columns:404px 404px;grid-template-rows:571px 571px;
    gap:20px;justify-content:center;align-content:center;height:1200px;
  }
  .page{position:relative;background:var(--sheet);overflow:hidden;width:404px;height:571px}

  /* Identity */
  .identity{text-align:center;color:var(--brand-blue)}
  .identity__name{font-weight:300;letter-spacing:.5px}
  .identity__role{font-weight:300;font-size:11px;margin-top:4px}

  /* Back page: contact */
  .page--contact .identity{position:absolute;top:68px;left:0;right:0}
  .page--contact .identity__name{font-size:21px}
  .contact{position:absolute;top:145px;left:0;right:0;text-align:center;color:var(--ink-navy);font-size:15px;line-height:20px;font-style:normal}
  .contact__line{display:flex;align-items:center;justify-content:center;gap:6px}
  .contact__line--mail{margin-top:5px}
  .contact__line--phone{margin-top:6px;font-weight:500}
  .contact__icon{width:15px;height:15px;fill:var(--brand-blue)}

  /* Cover */
  .page--cover .identity{position:absolute;top:140px;left:0;right:0}
  .page--cover .identity__name{font-size:25px}
  .page--cover .identity__role{font-size:12px;margin-top:10px}

  .visual{position:absolute;left:0;bottom:0;display:block}

  /* Inner pages */
  .wave{position:absolute;left:0;width:404px;display:block}
  .wave--top{top:0}
  .wave--bottom{bottom:0}

  .intro{position:absolute;top:56px;left:20px;right:22px}
  .intro__name{font-weight:400;font-size:15.5px;color:var(--ink-navy)}
  .intro__claim{font-weight:500;font-size:15px;color:var(--brand-cyan);margin-top:1px}
  .intro__text{font-size:7.6px;line-height:10px;margin-top:8px;color:var(--ink-body)}
  .intro__label{font-style:italic;font-size:11px;color:var(--ink-navy);margin-top:13px}

  .skills{position:absolute;top:168px;left:0;width:384px;display:flex;flex-direction:column;gap:12px}
  .skill{border:1px solid var(--brand-blue);border-left:none;border-radius:0 28px 28px 0;padding-bottom:7px}
  .skill__title{
    font-weight:700;font-size:11px;color:#fff;padding:2px 20px;
    background:linear-gradient(90deg,#3cb5df 0%,var(--brand-sky) 30%,var(--brand-ice) 62%,rgba(255,255,255,0) 95%);
  }
  .skill__list{list-style:none;padding:5px 0 0 20px;font-size:7.6px;line-height:9.6px;color:var(--ink-body);
    border-bottom:1px dashed #c8cdd2;margin-right:140px;padding-bottom:4px}
  .skill__list li{position:relative;padding-left:10px}
  .skill__list li::before{content:"";position:absolute;left:0;top:3px;width:3.5px;height:3.5px;border-radius:50%;background:var(--brand-blue)}
  .skill--wide .skill__list{margin-right:0;border-bottom:none;padding-right:6px}

  .heading{position:absolute;left:20px;font-weight:700;font-size:15px;color:var(--ink-navy)}
  .heading::after{content:"";display:block;width:52px;height:3px;background:var(--brand-sky);margin-top:3px}
  .heading--advantage{top:58px}
  .heading--unique{top:283px}

  .assets{position:absolute;top:92px;left:18px;right:18px;display:grid;grid-template-columns:1fr 1fr;column-gap:16px;row-gap:16px}
  .asset{position:relative;padding-left:30px;padding-top:22px;min-height:70px}
  .asset__num{position:absolute;left:0;top:0;font-weight:500;font-size:18px;color:var(--brand-cyan)}
  .asset__slash{position:absolute;left:4px;top:2px;width:42px;height:40px}
  .asset__title{font-weight:700;font-size:8px;line-height:10px;color:var(--ink-navy)}
  .asset__text{font-size:7px;line-height:9px;margin-top:4px;color:var(--ink-body)}

  .story{position:absolute;top:318px;left:20px;right:18px;font-size:7.6px;line-height:10px;color:var(--ink-body)}
  .story p + p{margin-top:9px}
</style>
</head>
<body>
<main class="spread">

  <!-- Page 4: contact -->
  <section class="page page--contact">
    <header class="identity">
      <p class="identity__name">Lucien Maréchal-Dorval</p>
      <p class="identity__role">Assistant de projet indépendant</p>
    </header>
    <address class="contact">
      <p>Ch. des Tilleuls 8</p>
      <p>1870 Montrey</p>
      <p class="contact__line contact__line--mail">
        <svg class="contact__icon" viewBox="0 0 24 24" aria-hidden="true"><path d="M2 5h20v14H2z" fill="none" stroke="#0094d4" stroke-width="2"/><path d="M2 5l10 8 10-8" fill="none" stroke="#0094d4" stroke-width="2"/></svg>
        lucien@marechal-dorval.ch
      </p>
      <p class="contact__line contact__line--phone">
        <svg class="contact__icon" viewBox="0 0 24 24" aria-hidden="true"><path d="M6.6 10.8a15.1 15.1 0 0 0 6.6 6.6l2.2-2.2c.3-.3.7-.4 1-.2 1.1.4 2.3.6 3.6.6.6 0 1 .4 1 1V20c0 .6-.4 1-1 1A17 17 0 0 1 3 4c0-.6.4-1 1-1h3.5c.6 0 1 .4 1 1 0 1.3.2 2.5.6 3.6.1.3 0 .7-.2 1z"/></svg>
        +41 78 512 30 46
      </p>
    </address>
    <svg class="visual" width="404" height="320" viewBox="0 0 404 320" role="img" aria-label="Photo de façade d'immeuble en verre vue en contre-plongée">
      <defs>
        <linearGradient id="contactSky" x1="0" y1="0" x2="1" y2="1">
          <stop offset="0" stop-color="#f1f3f5"/>
          <stop offset=".45" stop-color="#cfd6dc"/>
          <stop offset="1" stop-color="#9fb0bd"/>
        </linearGradient>
        <linearGradient id="contactGlass" x1="0" y1="0" x2="1" y2="1">
          <stop offset="0" stop-color="#4d88b8"/>
          <stop offset="1" stop-color="#17507f"/>
        </linearGradient>
      </defs>
      <path d="M0 120 Q 150 30 404 10 L404 320 L0 320Z" fill="url(#contactSky)"/>
      <path d="M0 250 Q 60 200 150 170 L404 60 L404 320 L0 320Z" fill="url(#contactGlass)"/>
      <path d="M0 250 Q 100 200 260 120 L404 60" fill="none" stroke="#ffffff" stroke-opacity=".5" stroke-width="2"/>
    </svg>
  </section>

  <!-- Page 1: cover -->
  <section class="page page--cover">
    <header class="identity">
      <h1 class="identity__name">Lucien Maréchal-Dorval</h1>
      <p class="identity__role">Assistant de projet indépendant</p>
    </header>
    <svg class="visual" width="404" height="340" viewBox="0 0 404 340" role="img" aria-label="Emplacement de la photo de profil devant une façade d'immeuble bleue">
      <defs>
        <linearGradient id="coverArc" x1="0" y1="0" x2="1" y2="1">
          <stop offset="0" stop-color="#2aa9d6"/>
          <stop offset=".5" stop-color="#1a7fb6"/>
          <stop offset="1" stop-color="#134c7c"/>
        </linearGradient>
        <linearGradient id="coverPortrait" x1="0" y1="0" x2="0" y2="1">
          <stop offset="0" stop-color="#e7ecef"/>
          <stop offset=".4" stop-color="#8aa8c2"/>
          <stop offset="1" stop-color="#4d6f92"/>
        </linearGradient>
      </defs>
      <path d="M0 150 Q 120 30 404 36 L404 340 L0 340Z" fill="url(#coverArc)"/>
      <path d="M0 190 Q 140 80 404 80" fill="none" stroke="#6fccea" stroke-opacity=".6" stroke-width="3"/>
      <rect x="75" y="20" width="210" height="330" rx="80" fill="url(#coverPortrait)" opacity=".9"/>
    </svg>
  </section>

  <!-- Page 2: expertise -->
  <section class="page page--expertise">
    <svg class="wave wave--top" height="52" viewBox="0 0 404 52" aria-hidden="true">
      <defs>
        <linearGradient id="waveBlue" x1="0" y1="0" x2="1" y2="0">
          <stop offset="0" stop-color="#3cc3e3"/>
          <stop offset=".6" stop-color="#0094d4"/>
          <stop offset="1" stop-color="#1b5f9b"/>
        </linearGradient>
      </defs>
      <path d="M0 0 H404 V10 Q 300 30 190 16 Q 80 2 0 40Z" fill="var(--wave-grey)"/>
      <path d="M0 0 H404 V4 Q 300 22 190 10 Q 80 -2 0 34Z" fill="url(#waveBlue)"/>
      <path d="M0 0 H240 Q 120 2 0 26Z" fill="#6fccea" opacity=".7"/>
    </svg>

    <div class="intro">
      <h2 class="intro__name">Lucien Maréchal-Dorval :</h2>
      <p class="intro__claim">Un atout précieux pour votre bureau d'études</p>
      <p class="intro__text">Avec plus de 30 ans d'expérience dans l'industrie, je suis un expert chevronné en conception, gestion de projets et sécurité. J'offre mes services d'assistant de projet indépendant pour vous aider à gérer les pics de charge et les besoins spécifiques de votre bureau d'études.</p>
      <p class="intro__label">Mon expertise :</p>
    </div>

    <div class="skills">
      <article class="skill">
        <h3 class="skill__title">Conception &amp; Design :</h3>
        <ul class="skill__list">
          <li>Maquettes 3D (PlantForge 3D)</li>
          <li>Plans, schémas, RI/P&amp;ID, Flowsheets</li>
          <li>Spécifications, catalogues, définition des fournitures</li>
        </ul>
      </article>
      <article class="skill">
        <h3 class="skill__title">Gestion de Projets :</h3>
        <ul class="skill__list">
          <li>Rédaction d'appels d'offre</li>
          <li>Préparation de budgets</li>
          <li>Réalisation de plannings</li>
          <li>Estimations budgétaires</li>
          <li>Réponse aux appels d'offre</li>
        </ul>
      </article>
      <article class="skill">
        <h3 class="skill__title">Sécurité :</h3>
        <ul class="skill__list">
          <li>Sécurité machine</li>
          <li>Plans de montage</li>
          <li>Edition de PHS</li>
        </ul>
      </article>
      <article class="skill">
        <h3 class="skill__title">Documentation Technique :</h3>
        <ul class="skill__list">
          <li>DESP</li>
          <li>Documentations spécifiques</li>
        </ul>
      </article>
      <article class="skill skill--wide">
        <h3 class="skill__title">Expertise :</h3>
        <ul class="skill__list">
          <li>Ma connaissance approfondie de la métallurgie (tuyauterie, serrurerie, chaudronnerie, charpente métallique, montage) me permet de garantir des études complètes et d'éviter les oublis.</li>
        </ul>
      </article>
    </div>

    <svg class="wave wave--bottom" height="40" viewBox="0 0 404 40" aria-hidden="true">
      <defs>
        <linearGradient id="waveBlueLow" x1="0" y1="0" x2="1" y2="0">
          <stop offset="0" stop-color="#1b5f9b"/>
          <stop offset=".5" stop-color="#0094d4"/>
          <stop offset="1" stop-color="#3cc3e3"/>
        </linearGradient>
      </defs>
      <path d="M0 14 Q 40 34 140 30 Q 290 22 404 2 V40 H0Z" fill="var(--wave-grey)"/>
      <path d="M0 22 Q 40 40 150 36 Q 290 30 404 12 V40 H0Z" fill="url(#waveBlueLow)"/>
    </svg>
  </section>

  <!-- Page 3: advantages -->
  <section class="page page--advantages">
    <svg class="wave wave--top" height="52" viewBox="0 0 404 52" aria-hidden="true">
      <defs>
        <linearGradient id="waveBlueR" x1="0" y1="0" x2="1" y2="0">
          <stop offset="0" stop-color="#1b5f9b"/>
          <stop offset=".5" stop-color="#0094d4"/>
          <stop offset="1" stop-color="#3cc3e3"/>
        </linearGradient>
      </defs>
      <path d="M0 0 H404 V44 Q 320 10 210 22 Q 90 34 0 14Z" fill="var(--wave-grey)"/>
      <path d="M0 0 H404 V36 Q 320 4 210 14 Q 90 26 0 8Z" fill="url(#waveBlueR)"/>
      <path d="M0 0 H130 Q 60 14 0 20Z" fill="#3cc3e3" opacity=".8"/>
    </svg>

    <h2 class="heading heading--advantage">Votre avantage :</h2>

    <div class="assets">
      <article class="asset">
        <svg class="asset__slash" viewBox="0 0 42 40" aria-hidden="true"><path d="M40 0 L6 38" stroke="#1c6fae" stroke-width="1.6"/></svg>
        <span class="asset__num">01</span>
        <h3 class="asset__title">Connaissance des besoins des concepteurs et des fabricants :</h3>
        <p class="asset__text">J'ai travaillé des deux côtés, ce qui me permet de comprendre les défis et les attentes de chacun.</p>
      </article>
      <article class="asset">
        <svg class="asset__slash" viewBox="0 0 42 40" aria-hidden="true"><path d="M40 0 L6 38" stroke="#1c6fae" stroke-width="1.6"/></svg>
        <span class="asset__num">02</span>
        <h3 class="asset__title">Flexibilité :</h3>
        <p class="asset__text">Je suis disponible pour des missions ponctuelles et à durée déterminée, sans engagement à long terme.</p>
      </article>
      <article class="asset">
        <svg class="asset__slash" viewBox="0 0 42 40" aria-hidden="true"><path d="M40 0 L6 38" stroke="#1c6fae" stroke-width="1.6"/></svg>
        <span class="asset__num">03</span>
        <h3 class="asset__title">Efficacité :</h3>
        <p class="asset__text">Je peux vous aider à gérer les surcharges de travail et à respecter vos délais.</p>
      </article>
      <article class="asset">
        <svg class="asset__slash" viewBox="0 0 42 40" aria-hidden="true"><path d="M40 0 L6 38" stroke="#1c6fae" stroke-width="1.6"/></svg>
        <span class="asset__num">04</span>
        <h3 class="asset__title">Collaboration fluide :</h3>
        <p class="asset__text">Je suis à votre disposition pour discuter de vos besoins et vous proposer des solutions sur mesure.</p>
      </article>
    </div>

    <h2 class="heading heading--unique">Un atout unique :</h2>
    <div class="story">
      <p>Malgré mon handicap en fauteuil roulant, je suis totalement opérationnel et mon expérience me permet de vous offrir une expertise de haut niveau. Je suis disponible à 35% dès septembre 2024 et je suis prêt à mettre mon expertise et mon dynamisme au service de votre succès.</p>
      <p>N'hésitez pas à me contacter pour discuter de vos besoins et découvrir comment je peux vous aider à atteindre vos objectifs</p>
    </div>

    <svg class="visual" width="404" height="175" viewBox="0 0 404 175" role="img" aria-label="Illustration de tours d'immeubles en perspective, traits bleus">
      <defs>
        <linearGradient id="towerTone" x1="0" y1="0" x2="0" y2="1">
          <stop offset="0" stop-color="#ffffff" stop-opacity="0"/>
          <stop offset=".4" stop-color="#c9d6e6"/>
          <stop offset="1" stop-color="#6f8fb8"/>
        </linearGradient>
        <linearGradient id="waveBlueLowR" x1="0" y1="0" x2="1" y2="0">
          <stop offset="0" stop-color="#3cc3e3"/>
          <stop offset=".5" stop-color="#0094d4"/>
          <stop offset="1" stop-color="#1b5f9b"/>
        </linearGradient>
      </defs>
      <rect x="0" y="20" width="404" height="155" fill="url(#towerTone)" opacity=".75"/>
      <path d="M0 148 Q 120 118 250 130 Q 340 138 404 120 V175 H0Z" fill="var(--wave-grey)"/>
      <path d="M0 158 Q 120 130 250 142 Q 340 150 404 132 V175 H0Z" fill="url(#waveBlueLowR)"/>
    </svg>
  </section>

</main>
</body>
</html>
```